Halloway Consulting Cover 2 - Smart Capital

Halloway Consulting is a business consulting firm. We will publish a series of four thought leadership pieces online and via PDF. The second of the series is attached to this project. We need an eye-catching cover page with a back page that keeps with our branding. The document attached is in the final draft, and the cover and pack pages are placeholders only. You can find more about our branding and style on our website www.hallowayconsulting.com.au. The other three projects can be found here with a similar brief, and you are welcome to submit a design for all 4.

```html
<!DOCTYPE html>
<html lang="en">
<head>
<meta charset="utf-8">
<title>Halloway Consulting – Smart Capital Cover, Back and Front</title>
<link rel="stylesheet" href="https://fonts.googleapis.com/css2?family=Poppins:wght@400;500;600;700&display=swap">
<style>
  :root{
    --stage:#5a5a5a;
    --white:#ffffff;
    --ink:#1c1c1c;
    --orange:#f7941d;
    --brand-blue:#1e9bd7;
    --blue-deep:#0a56a8;
    --ring-blue:#0c5eaf;
  }
  *{margin:0;padding:0;box-sizing:border-box}
  html,body{width:844px;height:1200px;overflow:hidden;background:var(--stage)}
  body{font-family:"Poppins",sans-serif;position:relative}

  .spread{position:absolute;left:11px;top:300px;width:822px;height:600px}
  .page-label{position:absolute;top:0;width:403px;text-align:center;color:var(--white);font-size:17px;font-weight:500}
  .page-label.back-label{left:0}
  .page-label.front-label{left:419px}
  .page-slot{position:absolute;top:36px;width:403px;height:560px;overflow:hidden;box-shadow:0 4px 12px rgba(0,0,0,.35)}
  .page-slot.back-slot{left:0}
  .page-slot.front-slot{left:419px}

  .page{position:absolute;left:0;top:0;width:720px;height:1000px;overflow:hidden;background:var(--white);transform:scale(0.56);transform-origin:0 0}
  .page-art{position:absolute;inset:0;width:720px;height:1000px}

  /* brand lockups */
  .brand{position:absolute;display:flex;align-items:center}
  .brand-dot{border-radius:50%;background:var(--orange);flex:none}
  .brand-name{font-weight:600;line-height:1.02;color:var(--brand-blue)}
  .front .brand{left:51px;top:70px;gap:22px}
  .front .brand-dot{width:96px;height:96px}
  .front .brand-name{font-size:38px}
  .back .brand{left:51px;top:66px;gap:12px}
  .back .brand-dot{width:54px;height:54px}
  .back .brand-name{font-size:21px}

  /* front */
  .headline{position:absolute;left:51px;top:318px;color:var(--white);font-weight:600}
  .headline .kicker{display:block;color:var(--orange);font-size:40px;line-height:1.25}
  .headline .big{display:block;font-size:57px;line-height:1.1}
  .headline .small{display:block;font-size:40px;line-height:1.25}
  .subtitle{position:absolute;left:56px;top:616px;padding-left:14px;border-left:3px solid var(--orange);color:var(--white);font-weight:600;font-size:18px;line-height:28px}
  .front-website{position:absolute;left:421px;top:896px;color:var(--white);font-size:16px}

  /* back */
  .follow{position:absolute;left:464px;top:74px;display:flex;align-items:center;gap:8px;color:var(--orange);font-size:13px}
  .follow-square{width:14px;height:14px;background:var(--ink)}
  .back-website{position:absolute;left:464px;top:97px;color:var(--brand-blue);font-size:16px}
  .cta{position:absolute;left:0;width:720px;top:556px;text-align:center;color:var(--white);font-size:17px;line-height:26px}
  .cta .brand-mention{color:var(--orange);font-weight:600}
  .cta .emphasis{font-weight:600}
  .contacts{position:absolute;left:51px;top:734px}
  .contact{margin-bottom:22px}
  .contact-name{color:var(--brand-blue);font-weight:600;font-size:20px;line-height:26px}
  .contact-role{color:var(--orange);font-size:15px;line-height:20px;margin-bottom:6px}
  .contact-line{display:flex;align-items:center;gap:14px;color:var(--ink);line-height:24px}
  .contact-line.phone{font-size:17px}
  .contact-line.email{font-size:13px}
  .contact-line svg{flex:none}
</style>
</head>
<body>
<section class="spread">
  <p class="page-label back-label">Back</p>
  <p class="page-label front-label">Front</p>

  <!-- back page -->
  <div class="page-slot back-slot">
    <article class="page back">
      <svg class="page-art" viewBox="0 0 720 1000">
        <defs>
          <linearGradient id="skyGrad" x1="0" y1="0" x2="1" y2="1">
            <stop offset="0" stop-color="#e4e4e4"/>
            <stop offset="1" stop-color="#f4f4f4"/>
          </linearGradient>
          <linearGradient id="backBand" x1="0" y1="0" x2="1" y2="1">
            <stop offset="0" stop-color="#0d6cc4"/>
            <stop offset="1" stop-color="#0a57ab"/>
          </linearGradient>
          <linearGradient id="backTower" x1="0" y1="0" x2="1" y2="1">
            <stop offset="0" stop-color="#7cc8f0"/>
            <stop offset="0.45" stop-color="#8a94a0"/>
            <stop offset="1" stop-color="#1c5fb0"/>
          </linearGradient>
        </defs>
        <rect x="0" y="0" width="720" height="300" fill="url(#skyGrad)" role="img" aria-label="Faint photo of office towers against the sky"/>
        <path d="M0 228 Q160 262 330 262 L720 262 L720 690 Q600 688 470 700 Q230 706 0 722 Z" fill="url(#backBand)" role="img" aria-label="Blue-tinted photo of glass skyscrapers"/>
        <circle cx="724" cy="1000" r="315" fill="#0c66bb"/>
        <circle cx="724" cy="1000" r="255" fill="none" stroke="#4a9ee2" stroke-width="24" opacity="0.7"/>
        <circle cx="724" cy="1000" r="222" fill="none" stroke="#a9d3f2" stroke-width="20" opacity="0.7"/>
        <circle cx="724" cy="1010" r="200" fill="var(--white)"/>
        <circle cx="360" cy="344" r="186" fill="#f7941d" opacity="0.85"/>
        <circle cx="360" cy="344" r="138" fill="var(--white)"/>
        <circle cx="360" cy="344" r="125" fill="url(#backTower)" role="img" aria-label="Photo of a glass tower facade"/>
      </svg>

      <div class="brand"><span class="brand-dot"></span><span class="brand-name">Halloway<br>Consulting</span></div>
      <p class="follow">Follow us: <span class="follow-square"></span></p>
      <p class="back-website">hallowayconsulting.com.au</p>

      <p class="cta">Contact us to find out how <span class="brand-mention">Halloway Consulting</span><br>can help build your company into a<br><span class="emphasis">Market Leader Today.</span></p>

      <div class="contacts">
        <div class="contact">
          <p class="contact-name">Martin Halloway</p>
          <p class="contact-role">Managing Director</p>
          <p class="contact-line phone"><svg width="14" height="14" viewBox="0 0 24 24"><path d="M6.6 10.8a15 15 0 0 0 6.6 6.6l2.2-2.2a1 1 0 0 1 1-.25 11.4 11.4 0 0 0 3.6.57 1 1 0 0 1 1 1V20a1 1 0 0 1-1 1A17 17 0 0 1 3 4a1 1 0 0 1 1-1h3.5a1 1 0 0 1 1 1c0 1.25.2 2.45.57 3.57a1 1 0 0 1-.25 1z" fill="#f7941d"/></svg>+61 400 555 018</p>
          <p class="contact-line email"><svg width="14" height="10" viewBox="0 0 14 10"><rect width="14" height="10" rx="1" fill="#f7941d"/><path d="M0 0l7 6 7-6" fill="none" stroke="#fff" stroke-width="1.2"/></svg>martin@hallowayconsulting.com.au</p>
        </div>
        <div class="contact">
          <p class="contact-name">Oliver Halloway</p>
          <p class="contact-role">Managing Director</p>
          <p class="contact-line phone"><svg width="14" height="14" viewBox="0 0 24 24"><path d="M6.6 10.8a15 15 0 0 0 6.6 6.6l2.2-2.2a1 1 0 0 1 1-.25 11.4 11.4 0 0 0 3.6.57 1 1 0 0 1 1 1V20a1 1 0 0 1-1 1A17 17 0 0 1 3 4a1 1 0 0 1 1-1h3.5a1 1 0 0 1 1 1c0 1.25.2 2.45.57 3.57a1 1 0 0 1-.25 1z" fill="#f7941d"/></svg>+61 400 555 027</p>
          <p class="contact-line email"><svg width="14" height="10" viewBox="0 0 14 10"><rect width="14" height="10" rx="1" fill="#f7941d"/><path d="M0 0l7 6 7-6" fill="none" stroke="#fff" stroke-width="1.2"/></svg>oliver@hallowayconsulting.com.au</p>
        </div>
      </div>
    </article>
  </div>

  <!-- front page -->
  <div class="page-slot front-slot">
    <article class="page front">
      <svg class="page-art" viewBox="0 0 720 1000">
        <defs>
          <linearGradient id="bandGrad" x1="0" y1="0" x2="1" y2="1">
            <stop offset="0" stop-color="#0a82cf"/>
            <stop offset="1" stop-color="#0a58ab"/>
          </linearGradient>
          <linearGradient id="towersGrad" x1="0" y1="0" x2="1" y2="1">
            <stop offset="0" stop-color="#1f79cf"/>
            <stop offset="0.5" stop-color="#0c5cb3"/>
            <stop offset="1" stop-color="#2d8ee0"/>
          </linearGradient>
          <linearGradient id="handsGrad" x1="0" y1="0" x2="1" y2="1">
            <stop offset="0" stop-color="#3a3430"/>
            <stop offset="0.55" stop-color="#8a6a55"/>
            <stop offset="1" stop-color="#c9c5c0"/>
          </linearGradient>
        </defs>
        <path d="M0 262 Q180 250 330 268 Q420 280 480 262 L720 262 L720 1000 L0 1000 Z" fill="url(#bandGrad)"/>
        <rect x="0" y="688" width="720" height="312" fill="url(#towersGrad)" role="img" aria-label="Photo of glass skyscrapers seen from below"/>
        <rect x="0" y="300" width="630" height="388" fill="#0b78c6" opacity="0.5"/>
        <circle cx="600" cy="410" r="275" fill="var(--ring-blue)"/>
        <circle cx="600" cy="410" r="190" fill="var(--white)"/>
        <circle cx="600" cy="410" r="176" fill="url(#handsGrad)" role="img" aria-label="Photo of two businesspeople bumping fists over a desk"/>
        <circle cx="100" cy="1045" r="262" fill="none" stroke="#5aa9e6" stroke-width="30" opacity="0.55"/>
        <circle cx="100" cy="1045" r="226" fill="none" stroke="#8cc6f0" stroke-width="20" opacity="0.6"/>
        <circle cx="100" cy="1045" r="210" fill="var(--white)"/>
      </svg>

      <div class="brand"><span class="brand-dot"></span><span class="brand-name">Halloway<br>Consulting</span></div>

      <h1 class="headline">
        <span class="kicker">Smart Capital:</span>
        <span class="big">Partnering</span>
        <span class="small">with funds to</span>
        <span class="big">Scale Your</span>
        <span class="big">Business</span>
      </h1>

      <p class="subtitle">Bridging Valuation Gaps in Fund Raising</p>
      <p class="front-website">hallowayconsulting.com.au</p>
    </article>
  </div>
</section>
</body>
</html>
```